Этикетка для Частная пивоварня " Корвенталь"
Опишите свою организацию или продукт и целевую аудиторию
Завод KORVENTAL построен и введен в эксплуатацию в 2015 году. Мы используем в процессе производства только натуральные ингредиенты высокого качества: немецкий хмель двух сортов и солод.
Целевая аудитория нашего пива- в основной массе мужчины.
Комментарии и пожелания для дизайнеров
Необходимо разработать концепт дизайна этикета на пиво « Тарвинское». Форма самой этикетки не принципиальна: может быть как прямоугольной, так и округлой формы. Главное требование-она должна гармонично сочетаться с формой бутылки.
Цветовая гамма для Тарвинского–готовы рассмотреть варианты: как сине-желто-белая, так и бежевая. Хотелось бы привлечь клиента узнаваемым дизайном пива «Тарвинское», ретро -стиль, но в то же время этикетка должна отличаться от представленных на рынке.
О производителе на этикетке будет говорить лишь фирменный логотип.
Обязательная информация на лицевую часть: « пиво светлое пастеризованное», « настоящее живое», « изготовлено из натуральных ингредиентов».
Контрэтикетка будет содержать текстовую часть( информация о составе, производителе, информацию для потребителя).
Планируем печать на льне. В качестве логотипа используется буква в обрамлении.

```html
<!DOCTYPE html>
<html lang="ru">
<head>
<meta charset="utf-8">
<title>Пиво Тарвинское — этикетка</title>
<link href="https://fonts.googleapis.com/css2?family=Oswald:wght@400;500;700&family=Marck+Script&display=swap" rel="stylesheet">
<style>
  :root {
    --page-bg: #ffffff;
    --label-blue: #1e5b84;
    --label-blue-deep: #174a6e;
    --label-blue-light: #2a6a94;
    --title-yellow: #f6c21a;
    --title-shadow: #0f2e45;
    --ink-light: #e8eef2;
    --ink-soft: #c9d6df;
  }
  html, body {
    margin: 0;
    padding: 0;
    width: 1200px;
    height: 895px;
    overflow: hidden;
    background: var(--page-bg);
  }
  .canvas {
    position: relative;
    width: 1200px;
    height: 895px;
  }
  .label {
    position: absolute;
    left: 220px;
    top: 193px;
    width: 377px;
    height: 510px;
    background:
      radial-gradient(ellipse at 30% 25%, var(--label-blue-light) 0%, transparent 60%),
      radial-gradient(ellipse at 80% 85%, var(--label-blue-deep) 0%, transparent 65%),
      var(--label-blue);
    color: var(--ink-light);
    text-align: center;
    font-family: "Oswald", sans-serif;
  }
  .brand-mark {
    position: absolute;
    top: 52px;
    left: 0;
    right: 0;
    display: flex;
    justify-content: center;
    align-items: center;
    gap: 7px;
    font-family: "Oswald", sans-serif;
    font-weight: 500;
    font-size: 15px;
    letter-spacing: 1px;
    color: var(--ink-light);
  }
  .brand-mark .dot {
    width: 9px;
    height: 9px;
    border-radius: 50%;
    background: var(--ink-light);
  }
  .product-kind {
    position: absolute;
    top: 160px;
    left: 0;
    right: 0;
    font-family: "Marck Script", cursive;
    font-size: 40px;
    line-height: 1;
    color: var(--ink-light);
  }
  .product-name {
    position: absolute;
    top: 212px;
    left: 0;
    right: 0;
    font-family: "Oswald", sans-serif;
    font-weight: 700;
    font-size: 50px;
    line-height: 1;
    letter-spacing: 0.5px;
    color: var(--title-yellow);
    text-shadow: 2px 3px 0 var(--title-shadow);
  }
  .spec-row {
    position: absolute;
    top: 293px;
    left: 0;
    right: 0;
    display: flex;
    justify-content: center;
    align-items: center;
    gap: 10px;
  }
  .spec-row .spec-small {
    font-size: 6px;
    line-height: 1.1;
    color: var(--ink-soft);
    text-align: center;
  }
  .spec-row .spec-type {
    font-size: 14px;
    font-weight: 400;
    letter-spacing: 0.6px;
    color: var(--ink-light);
  }
  .claim {
    position: absolute;
    top: 437px;
    left: 0;
    right: 0;
    font-size: 13px;
    font-weight: 500;
    letter-spacing: 1px;
    word-spacing: 5px;
    color: var(--ink-light);
  }
  .ingredients {
    position: absolute;
    top: 460px;
    left: 0;
    right: 0;
    font-family: "Marck Script", cursive;
    font-size: 15px;
    color: var(--ink-soft);
  }
</style>
</head>
<body>
  <main class="canvas">
    <section class="label">
      <div class="brand-mark"><span class="dot"></span>КОРВЕНТАЛЬ</div>
      <div class="product-kind">Пиво</div>
      <h1 class="product-name" style="margin:0">ТАРВИНСКОЕ</h1>
      <div class="spec-row">
        <span class="spec-small">4,5%<br>АЛК</span>
        <span class="spec-type">СВЕТЛОЕ ПАСТЕРИЗОВАННОЕ</span>
        <span class="spec-small">500<br>МЛ</span>
      </div>
      <div class="claim">НАСТОЯЩЕЕ ЖИВОЕ</div>
      <div class="ingredients">Изготовлено из натуральных ингредиентов</div>
    </section>
  </main>
</body>
</html>
```